Tranquil Pathway Business Card

Logo attached. (will be printing onto thick white/off white textured card)

Double sided business card for two Therapists working at Tranquil Pathway.

Require one design, but with different name and mobile numbers on each card.

Target Market(s)

Medical, Health

Industry/Entity Type

Business

Contact Information for Business Card

Need one business card design, but a separate card for each person - Colin Marchetti and Marieke de Boeckx.

FRONT OF CARD

Logo

Name (Colin Marchetti on one card, Marieke de Boeckx on the other)
Professional Clinical Hypnotherapist

Consulting Rooms (Near Lindqvist Hospital)
482 Brackenfield Road
Dunmore VIC 3987

Colin@TranquilPathway.example.au OR Marieke@TranquilPathway.example.au

Mobile: 0455 872 604 (for Colin) OR
Mobile: 0467 290 518 (for Marieke)

BACK OF CARD

Logo

Website: www.TranquilPathway.example.au

Phone: 1300 958 471

Requirements
Must have
• Text and logo only. No additiional graphics.

```html
<!DOCTYPE html>
<html lang="en">
<head>
<meta charset="utf-8">
<title>Tranquil Pathway Business Card</title>
<link href="https://fonts.googleapis.com/css2?family=Arimo:wght@400;700&display=swap" rel="stylesheet">
<style>
  :root {
    --backdrop: #1f1f21;
    --card: #77787b;
    --navy: #1c2559;
    --ring: #f2f2f2;
    --ink: #ffffff;
  }
  * { box-sizing: border-box; margin: 0; padding: 0; }
  html, body { width: 1200px; height: 800px; overflow: hidden; }
  body {
    background: var(--backdrop);
    font-family: "Arimo", Arial, sans-serif;
    color: var(--ink);
    position: relative;
  }
  .card {
    position: absolute;
    width: 780px;
    height: 340px;
    background: var(--card);
  }
  .card--front { left: 210px; top: 45px; border-radius: 170px 14px 14px 170px; }
  .card--back  { left: 210px; top: 415px; border-radius: 14px 170px 170px 14px; }

  .brand-disc {
    position: absolute;
    top: 22px;
    width: 296px;
    height: 296px;
    border-radius: 50%;
    background: var(--navy);
    border: 12px solid var(--ring);
    display: flex;
    align-items: center;
    justify-content: center;
    text-align: center;
  }
  .card--front .brand-disc { left: 22px; }
  .card--back .brand-disc { right: 22px; }
  .brand-name {
    font-weight: 700;
    font-size: 34px;
    line-height: 1.15;
    color: var(--ink);
    width: 200px;
  }

  .details {
    position: absolute;
    top: 34px;
    right: 40px;
    width: 400px;
    text-align: center;
  }
  .person-name {
    font-weight: 700;
    font-size: 28px;
    font-variant: small-caps;
    letter-spacing: 1px;
  }
  .person-role {
    font-weight: 700;
    font-size: 14px;
    font-variant: small-caps;
    letter-spacing: 1.5px;
    color: var(--navy);
    margin-bottom: 16px;
  }
  .contact-item { margin-bottom: 10px; }
  .icon {
    display: block;
    margin: 0 auto 5px;
    width: 24px;
    height: 24px;
  }
  .contact-text {
    font-weight: 700;
    font-size: 15px;
    line-height: 1.3;
  }

  .back-details {
    position: absolute;
    left: 60px;
    top: 100px;
    width: 340px;
    text-align: center;
  }
  .back-details .contact-item { margin-bottom: 26px; }
</style>
</head>
<body>

<section class="card card--front" aria-label="Card front">
  <div class="brand-disc"><span class="brand-name">Tranquil Pathway</span></div>
  <div class="details">
    <h1 class="person-name">Colin Marchetti</h1>
    <p class="person-role">Professional Clinical Hypnotherapist</p>

    <div class="contact-item">
      <svg class="icon" viewBox="0 0 24 24" aria-hidden="true">
        <circle cx="12" cy="12" r="12" fill="var(--navy)"/>
        <path d="M12 5.5a4 4 0 0 0-4 4c0 3 4 8 4 8s4-5 4-8a4 4 0 0 0-4-4z" fill="#8a90b8"/>
        <circle cx="12" cy="9.5" r="1.5" fill="var(--navy)"/>
      </svg>
      <p class="contact-text">Consulting Rooms (Near Lindqvist Hospital)<br>482 Brackenfield Road<br>Dunmore VIC 3987</p>
    </div>

    <div class="contact-item">
      <svg class="icon" viewBox="0 0 24 24" aria-hidden="true">
        <circle cx="12" cy="12" r="12" fill="var(--navy)"/>
        <path d="M8.5 6.5l2 2.5-1.2 1.3c.8 1.7 2 2.9 3.7 3.7l1.3-1.2 2.5 2-1.3 1.7c-4 0-8.7-4.7-8.7-8.7z" fill="#8a90b8"/>
      </svg>
      <p class="contact-text">0455 872 604</p>
    </div>

    <div class="contact-item">
      <svg class="icon" viewBox="0 0 24 24" aria-hidden="true">
        <circle cx="12" cy="12" r="12" fill="var(--navy)"/>
        <rect x="6" y="8" width="12" height="8.5" rx="1" fill="#8a90b8"/>
        <path d="M6.5 8.5l5.5 4.2 5.5-4.2" fill="none" stroke="var(--navy)" stroke-width="1.2"/>
      </svg>
      <p class="contact-text">Colin@TranquilPathway.example.au</p>
    </div>
  </div>
</section>

<section class="card card--back" aria-label="Card back">
  <div class="back-details">
    <div class="contact-item">
      <svg class="icon" viewBox="0 0 24 24" aria-hidden="true">
        <circle cx="12" cy="12" r="12" fill="var(--navy)"/>
        <circle cx="12" cy="12" r="6" fill="none" stroke="#8a90b8" stroke-width="1.3"/>
        <ellipse cx="12" cy="12" rx="2.6" ry="6" fill="none" stroke="#8a90b8" stroke-width="1.1"/>
        <path d="M6 12h12" stroke="#8a90b8" stroke-width="1.1"/>
      </svg>
      <p class="contact-text">www.TranquilPathway.example.au</p>
    </div>
    <div class="contact-item">
      <svg class="icon" viewBox="0 0 24 24" aria-hidden="true">
        <circle cx="12" cy="12" r="12" fill="var(--navy)"/>
        <path d="M8.5 6.5l2 2.5-1.2 1.3c.8 1.7 2 2.9 3.7 3.7l1.3-1.2 2.5 2-1.3 1.7c-4 0-8.7-4.7-8.7-8.7z" fill="#8a90b8"/>
      </svg>
      <p class="contact-text">1300 958 471</p>
    </div>
  </div>
  <div class="brand-disc"><span class="brand-name">Tranquil Pathway</span></div>
</section>

</body>
</html>
```